Lawn care business card

I am looking for a quality designed personal business card to represent the quality and elegant nature of our company. We separate ourselves in our market by the aesthetic value of our work, so I am looking for marketing material that does the same. We target our marketing high end customers, and we try to avoid price shoppers. I am open to all design options, so long as they are in line with our companies values.

We are tend to go with a retro look on everything from our logo and print material, to our uniforms. We like to portray and "old fashion" set of core values, with a modern elegance. So a wild and crazy look is out of the question.

Things I'd like on the card:
1.) Logo
2.) Phone number: (816) 555-0193
3.) Website: Verdanthollow.com
4.) Email: peterwalsh@verdanthollow.com
5.) My name: Peter Walsh
6.) Facebook link: facebook.com/GreenridgeLawnandLandscape
7.) Instagram: http://instagram.com/verdanthollow

Attached is a copy of our logo.

```html
<!DOCTYPE html>
<html lang="en">
<head>
<meta charset="utf-8">
<title>Verdant Hollow – Business Card</title>
<link rel="stylesheet" href="https://fonts.googleapis.com/css2?family=Lato:wght@400;700;900&display=swap">
<style>
  :root {
    --backdrop: #2c2c2c;
    --card-white: #f6f6f6;
    --brand-orange: #e4530f;
    --brand-orange-deep: #c6420a;
    --ink: #242424;
    --on-orange: #ffffff;
  }
  * { box-sizing: border-box; margin: 0; padding: 0; }
  html, body {
    width: 1200px; height: 1116px; overflow: hidden;
    background: var(--backdrop);
    font-family: "Lato", sans-serif;
  }
  .card {
    position: absolute; left: 75px; top: 258px;
    width: 1050px; height: 600px;
    border-radius: 28px; overflow: hidden;
    background: var(--card-white);
  }
  .card__band {
    position: absolute; left: 0; right: 0; top: 330px; bottom: 0;
    background: linear-gradient(100deg, var(--brand-orange) 0%, var(--brand-orange-deep) 100%);
  }
  .holder {
    position: absolute; left: 62px; top: 172px;
    display: flex; align-items: baseline; gap: 14px;
  }
  .holder__name { font-size: 40px; font-weight: 400; color: var(--brand-orange); }
  .holder__name strong { font-weight: 700; }
  .holder__role { font-size: 19px; font-weight: 700; color: var(--ink); transform: translateY(-16px); }
  .brand {
    position: absolute; right: 70px; top: 90px;
    display: flex; align-items: center; gap: 20px;
  }
  .brand__dot { width: 84px; height: 84px; border-radius: 50%; background: var(--brand-orange); }
  .brand__name { font-size: 44px; font-weight: 900; color: var(--ink); letter-spacing: 1px; text-transform: uppercase; }
  .contact {
    position: absolute; display: flex; flex-direction: column; gap: 14px;
    color: var(--on-orange); font-size: 22px; font-weight: 400;
  }
  .contact--direct { right: 48px; top: 352px; align-items: flex-end; }
  .contact--social { left: 48px; top: 432px; align-items: flex-end; }
  .contact__row { display: flex; align-items: center; gap: 14px; white-space: nowrap; }
  .contact__icon {
    width: 42px; height: 42px; border-radius: 50%;
    background: var(--on-orange); flex: none;
    display: flex; align-items: center; justify-content: center;
  }
  .contact__icon svg { width: 24px; height: 24px; }
  .website {
    position: absolute; left: 0; right: 0; top: 548px; text-align: center;
    font-size: 22px; font-weight: 900; color: var(--ink); letter-spacing: 5px;
  }
</style>
</head>
<body>
  <main class="card">
    <div class="card__band"></div>

    <div class="holder">
      <span class="holder__name">Peter <strong>Walsh</strong></span>
      <span class="holder__role">owner</span>
    </div>

    <div class="brand">
      <span class="brand__dot"></span>
      <span class="brand__name">Verdant Hollow</span>
    </div>

    <div class="contact contact--direct">
      <div class="contact__row">
        <span>(816) 555-0193</span>
        <span class="contact__icon">
          <svg viewBox="0 0 24 24" aria-hidden="true"><path fill="#e4530f" d="M6.6 10.8a15.1 15.1 0 0 0 6.6 6.6l2.2-2.2a1 1 0 0 1 1-.25 11.4 11.4 0 0 0 3.6.57 1 1 0 0 1 1 1V20a1 1 0 0 1-1 1A17 17 0 0 1 3 4a1 1 0 0 1 1-1h3.5a1 1 0 0 1 1 1c0 1.250.2 2.45.57 3.57a1 1 0 0 1-.25 1z"/></svg>
        </span>
      </div>
      <div class="contact__row">
        <span>peterwalsh@verdanthollow.com</span>
        <span class="contact__icon">
          <svg viewBox="0 0 24 24" aria-hidden="true"><rect x="3" y="6" width="18" height="12" rx="1.5" fill="#e4530f"/><path d="M3.5 7l8.5 6 8.5-6" fill="none" stroke="#fff" stroke-width="1.6"/></svg>
        </span>
      </div>
    </div>

    <div class="contact contact--social">
      <div class="contact__row">
        <span>snapgrove.com/verdanthollow</span>
        <span class="contact__icon"></span>
      </div>
      <div class="contact__row">
        <span>neighborly.com/GreenridgeLawnandLandscape</span>
        <span class="contact__icon"></span>
      </div>
    </div>

    <div class="website">www.verdanthollow.com</div>
  </main>
</body>
</html>
```